Marlow Crest Group (Real Estate and Investment)

A high end, clean design.
We are a real estate company with sales, asset management and investment divisions. We want to use a black and white scheme which is really high end feel. The back of the card can just be the logo (black background with the white writing) as we will probably emboss this when we print)

Target Market(s)

High level investors, high end houses for sale

Industry/Entity Type

Business

Contact Information for Business Card

Name, position, phone number and email address
Glen Varley, Managing Director, 0437259064 and glen@marlowcrest-example.com.au

Requirements
Must have
• Back of the card to be the black background with the white writing (as per the attached images). Would like the capacity to emboss the writing and logo

```html
<!DOCTYPE html>
<html lang="en">
<head>
<meta charset="utf-8">
<title>Marlow Crest Group – Glen Varley</title>
<link rel="stylesheet" href="https://fonts.googleapis.com/css2?family=Jura:wght@400;500;600&display=swap">
<style>
  :root {
    --card-black: #000000;
    --ink-white: #ffffff;
    --rule-white: #f4f4f4;
  }
  html, body {
    margin: 0;
    padding: 0;
    overflow: hidden;
    background: var(--card-black);
  }
  .business-card {
    position: relative;
    width: 1200px;
    height: 702px;
    background: var(--card-black);
    overflow: hidden;
    font-family: "Jura", sans-serif;
    color: var(--ink-white);
  }
  .brand-name {
    position: absolute;
    left: 303px;
    top: 356px;
    transform: translate(-50%, -50%);
    margin: 0;
    font-family: "Jura", sans-serif;
    font-weight: 500;
    font-size: 34px;
    line-height: 1.25;
    letter-spacing: 0.06em;
    text-align: center;
    text-transform: uppercase;
    color: var(--ink-white);
    white-space: nowrap;
  }
  .divider-rule {
    position: absolute;
    left: 0;
    top: 0;
  }
  .contact-block {
    position: absolute;
    left: 662px;
    top: 268px;
  }
  .person-name {
    margin: 0;
    font-family: "Jura", sans-serif;
    font-weight: 500;
    font-size: 44px;
    line-height: 58px;
    letter-spacing: 0.07em;
    text-transform: uppercase;
    white-space: nowrap;
  }
  .name-initial {
    font-size: 58px;
    font-weight: 600;
  }
  .contact-line {
    margin: 0;
    font-family: "Jura", sans-serif;
    font-weight: 400;
    font-size: 26px;
    line-height: 34px;
    letter-spacing: 0.01em;
    white-space: nowrap;
  }
  .contact-role {
    margin-top: 4px;
  }
</style>
</head>
<body>
  <main class="business-card">
    <p class="brand-name">Marlow Crest<br>Group</p>

    <svg class="divider-rule" width="1200" height="702" viewBox="0 0 1200 702" aria-hidden="true">
      <line x1="599.5" y1="69" x2="594.5" y2="629" stroke="var(--rule-white)" stroke-width="4"/>
    </svg>

    <section class="contact-block">
      <h1 class="person-name"><span class="name-initial">G</span>len <span class="name-initial">V</span>arley</h1>
      <p class="contact-line contact-role">Managing Director</p>
      <p class="contact-line contact-phone">0437259064</p>
      <p class="contact-line contact-email">glen@marlowcrest-example.com.au</p>
    </section>
  </main>
</body>
</html>
```